Design Christmas Carnival Marketing Material

Design Required ( Please submit design for this for selection)
- A4 Marketing Flyer ( infomation of events highlight, Christmas activities, Buffet Dinner, Call to action topurchase ticket online)

(Once shortlisted will proceed with the remainding designs)
- Facebook Marketing Advertisement ( Events highlights)
- Facebook Marketing Advertisement ( Christmas activities - artificial snow )
- Facebook Marketing Advertisement ( Buffet Dinner)

Theme is: Mythical Christmas with Pegasus ( Unicorns)

Events Highlights
-A quaint carnival in an enchanted nature fairground with alluring lighting that welcome childrens
-snow men and reindeer at Frostmere Glade
-Mingle with Unicorns, Mediveal Princess and Fairies
-Help Santa and his elves in simple games at Santa Workshop
-Indulge in delicious premium spread of Christmas Dinner Buffet with turkey, ham , prime ribs etc

Photo attachment are description of events, actual design do not need to include the description jus the title

```html
<!DOCTYPE html>
<html lang="en">
<head>
<meta charset="utf-8">
<title>Christmas Carnival Flyer</title>
<link rel="stylesheet" href="https://fonts.googleapis.com/css2?family=Pacifico&family=Alfa+Slab+One&family=Comic+Neue:wght@400;700&family=Cinzel:wght@700&display=swap">
<style>
  :root {
    --backdrop: #e9e6e1;
    --frame: #ffffff;
    --olive-deep: #3f3f1c;
    --red: #e0252b;
    --red-deep: #9e1016;
    --white: #ffffff;
    --aqua: #86f0e6;
  }
  * { margin: 0; padding: 0; box-sizing: border-box; }
  html, body { width: 1200px; height: 1164px; overflow: hidden; background: var(--backdrop); }
  .flyer {
    position: absolute; left: 210px; top: 30px;
    width: 780px; height: 1104px;
    border: 7px solid var(--frame);
    box-shadow: 0 6px 24px rgba(0,0,0,.25);
    overflow: hidden;
    background: var(--olive-deep);
  }
  .art-garland {
    position: absolute; left: 0; top: 0; width: 100%; height: 285px;
    background:
      radial-gradient(circle at 88% 30%, rgba(214,168,70,.9) 0 6%, transparent 12%),
      radial-gradient(circle at 60% 25%, rgba(214,168,70,.8) 0 5%, transparent 10%),
      radial-gradient(circle at 12% 20%, rgba(180,90,40,.85) 0 7%, transparent 14%),
      radial-gradient(ellipse at 50% 75%, #b9aeb0 0 30%, transparent 60%),
      linear-gradient(180deg, #29461f 0%, #3f5a2a 35%, #8a7f6e 75%, #6d6b4a 100%);
  }
  .art-tree {
    position: absolute; left: 0; top: 285px; width: 100%; height: 595px;
    background:
      radial-gradient(ellipse at 40% 45%, rgba(140,150,90,.7) 0 20%, transparent 50%),
      linear-gradient(180deg, #6a6a3a 0%, #5b5a2c 45%, #4b4a24 100%);
  }
  .art-gifts {
    position: absolute; left: 0; bottom: 0; width: 100%; height: 210px;
    background:
      radial-gradient(ellipse at 80% 50%, #7a6a38 0 25%, transparent 50%),
      linear-gradient(90deg, #8e1a1c 0%, #3e6a2e 35%, #a83a3a 60%, #5a4a28 100%);
  }
  .title {
    position: absolute; left: 0; top: 282px; width: 100%; text-align: center;
    font-family: 'Pacifico', cursive; font-weight: 400;
    font-size: 124px; line-height: 1.1;
    color: var(--white);
    -webkit-text-stroke: 4px var(--red);
    paint-order: stroke fill;
    text-shadow: 0 3px 4px rgba(0,0,0,.35);
  }
  .subtitle {
    position: absolute; right: 86px; top: 446px;
    font-family: 'Alfa Slab One', serif; font-style: italic;
    font-size: 54px; line-height: 1; color: var(--red);
    -webkit-text-stroke: 3px var(--white);
    paint-order: stroke fill;
  }
  .events-heading {
    position: absolute; left: 48px; top: 514px;
    font-family: 'Cinzel', serif; font-size: 32px; line-height: 1; color: var(--white);
    text-shadow: 0 2px 3px rgba(0,0,0,.4);
  }
  .events-list {
    position: absolute; left: 40px; top: 572px; width: 660px;
    list-style: none;
    font-family: 'Comic Neue', sans-serif; font-weight: 700;
    font-size: 17px; line-height: 1.25;
  }
  .events-list li {
    display: flex; align-items: flex-start; gap: 14px;
    margin-bottom: 16px;
    text-shadow: 0 1px 2px rgba(0,0,0,.5);
  }
  .events-list li:nth-child(odd) { color: var(--aqua); }
  .events-list li:nth-child(even) { color: var(--white); }
  .snowflake { flex: 0 0 24px; width: 24px; height: 24px; }
  .ticket-cta {
    position: absolute; left: 80px; top: 806px;
    display: inline-flex; align-items: center; gap: 12px;
    padding: 10px 26px;
    background: var(--red); border: 2px solid var(--white); border-radius: 26px;
    font-family: 'Comic Neue', sans-serif; font-weight: 700;
    font-size: 20px; line-height: 1; color: var(--white);
    box-shadow: 0 3px 8px rgba(0,0,0,.35);
  }
  .ticket-cta svg { width: 20px; height: 20px; }
</style>
</head>
<body>
  <main class="flyer">
    <div class="art-garland" role="img" aria-label="Pine garland with gold stars, bells and baubles"></div>
    <div class="art-tree" role="img" aria-label="Softly lit decorated Christmas tree in an enchanted forest"></div>
    <div class="art-gifts" role="img" aria-label="Wrapped Christmas gifts beside a pine branch"></div>

    <h1 class="title">Christmas</h1>
    <div class="subtitle">Carnival</div>

    <h2 class="events-heading">Events</h2>

    <svg width="0" height="0" style="position:absolute">
      <defs>
        <g id="flake" stroke="#fff" stroke-width="2.4" stroke-linecap="round" fill="none">
          <line x1="12" y1="2" x2="12" y2="22"/>
          <line x1="3.3" y1="7" x2="20.7" y2="17"/>
          <line x1="3.3" y1="17" x2="20.7" y2="7"/>
          <circle cx="12" cy="12" r="3.2"/>
        </g>
      </defs>
    </svg>

    <ul class="events-list">
      <li><svg class="snowflake" viewBox="0 0 24 24"><use href="#flake"/></svg><span>A quaint carnival in an enchanted nature fairground<br>with alluring lighting that welcome childrens</span></li>
      <li><svg class="snowflake" viewBox="0 0 24 24"><use href="#flake"/></svg><span>snow men and reindeer at Frostmere Glade</span></li>
      <li><svg class="snowflake" viewBox="0 0 24 24"><use href="#flake"/></svg><span>Mingle with Unicorns, Mediveal Princess and Fairies</span></li>
      <li><svg class="snowflake" viewBox="0 0 24 24"><use href="#flake"/></svg><span>Help Santa and his elves in simple games at Santa Workshop</span></li>
      <li><svg class="snowflake" viewBox="0 0 24 24"><use href="#flake"/></svg><span>Indulge in delicious premium spread of Christmas Dinner Buffet<br>with turkey, ham , prime ribs etc</span></li>
    </ul>

    <div class="ticket-cta">
      <span>Buy your tickets online now</span>
      <svg viewBox="0 0 20 20" aria-hidden="true"><path d="M4 10h11M10 4l6 6-6 6" stroke="#fff" stroke-width="2.6" fill="none" stroke-linecap="round" stroke-linejoin="round"/></svg>
    </div>
  </main>
</body>
</html>
```